Label for a new skin care product

Hello, we are launching a new skin care product. It's a face serum. One product only. I have attached the size requirements and a very general look at what is required. The final result will be a label sticker than gets placed on the bottle.

I have created some (amateur) designs using Canva here: https://www.plorvix.com/design/KTWmbHaxq3P/rQyTnnLoUsd_-JkZ_7_Xd_q/view?utm_content=KTWmbHaxq3P&utm_campaign=designshare&utm_medium=link2&utm_source=sharebutton

The text is what is required on the label. The design we are seeking is a very simply Wordmark logo with interesting font only. You can see I'm seeking ideas on a colorful design as well as something more ordinary/clinical. The people who will buy this product will be more upper class, well paid, and critical thinkers. Upscale. We don't want too many colors due to printing costs.

Target Market(s)

Female 25-45 years old who are hip and savvy

Requirements
Must have
• wordmark logo

```html
<!DOCTYPE html>
<html lang="en">
<head>
<meta charset="utf-8">
<title>Veyra Snail Mucin Essence – Label</title>
<link rel="stylesheet" href="https://fonts.googleapis.com/css2?family=Abril+Fatface&family=Josefin+Sans:ital,wght@0,400;0,600;1,400;1,600&family=Playfair+Display:ital@1&family=Nanum+Myeongjo:wght@700&display=swap">
<style>
  :root {
    --pink: #ec4f97;
    --pink-soft: #f9c9de;
    --ink: #333333;
    --grey: #4a4a4a;
    --paper: #ffffff;
    --page: #f3f1ef;
  }
  * { margin: 0; padding: 0; box-sizing: border-box; }
  html, body { width: 1200px; height: 818px; overflow: hidden; background: var(--page); }
  .label {
    position: absolute; left: 100px; top: 82px; width: 1000px; height: 654px;
    background: var(--paper);
    box-shadow: 2px 3px 4px rgba(0,0,0,.35);
    font-family: "Josefin Sans", sans-serif; color: var(--ink);
    overflow: hidden;
  }
  .label > * { position: absolute; }
  .heading {
    font-family: "Abril Fatface", serif; color: var(--pink);
    text-align: center; line-height: .9; font-size: 35px; letter-spacing: .5px;
  }
  .product-title { left: 40px; width: 260px; top: 67px; }
  .ingredients-title { left: 700px; width: 258px; top: 65px; }
  .copy { font-size: 15.5px; line-height: 17px; text-align: justify; text-align-last: left; }
  .directions { left: 41px; top: 230px; width: 256px; }
  .caution { left: 41px; top: 353px; width: 256px; }
  .care-icons { left: 84px; top: 424px; width: 172px; height: 56px; }
  .pill {
    background: var(--pink); color: #fff; font-size: 15px; font-weight: 600;
    display: flex; align-items: center; justify-content: center; padding-top: 3px;
  }
  .volume { left: 75px; top: 553px; width: 177px; height: 30px; }
  .floral-art {
    left: 515px; top: 12px; width: 185px; height: 642px;
    background: linear-gradient(180deg, rgba(249,201,222,.55), rgba(236,79,151,.22) 55%, rgba(249,201,222,.5));
    border-radius: 90px 90px 0 0;
  }
  .wordmark {
    left: 346px; top: 52px; font-family: "Abril Fatface", serif;
    font-size: 82px; color: var(--grey); line-height: 1;
  }
  .strength {
    left: 348px; top: 264px; font-family: "Playfair Display", serif; font-style: italic;
    font-size: 52px; color: var(--grey); line-height: 1;
  }
  .hero-name {
    left: 350px; top: 318px; font-family: "Abril Fatface", serif; color: var(--pink);
    font-size: 66px; line-height: .86;
  }
  .subtitle { left: 350px; top: 441px; font-size: 21px; line-height: 19px; font-style: italic; color: var(--ink); }
  .subtitle .accent { color: var(--pink); }
  .free-from { left: 350px; top: 492px; font-size: 13px; line-height: 14px; font-style: italic; font-weight: 600; color: var(--ink); }
  .korean { font-family: "Nanum Myeongjo", serif; font-weight: 700; color: var(--ink); }
  .tagline-ko { left: 348px; top: 598px; font-size: 24px; letter-spacing: 1px; }
  .centered { text-align: center; }
  .actives { left: 700px; width: 258px; top: 162px; font-size: 15.5px; line-height: 17px; }
  .rule { height: 2px; background: var(--pink); left: 766px; width: 127px; }
  .rule-top { top: 225px; }
  .rule-bottom { top: 419px; }
  .description { left: 702px; top: 240px; width: 256px; }
  .benefits-ko { left: 700px; top: 372px; width: 262px; font-size: 16px; line-height: 20px; text-align: center; }
  .benefits { left: 702px; top: 437px; width: 256px; }
  .website { left: 744px; top: 523px; width: 176px; height: 30px; }
  .promise { left: 700px; width: 258px; top: 570px; font-size: 17px; text-align: center; }
</style>
</head>
<body>
  <main class="label">
    <h2 class="heading product-title">SNAIL MUCIN<br>ESSENCE</h2>

    <p class="copy directions">Directions: For a pretty, natural glow apply AM and PM to freshly cleansed face, before all other actives.</p>
    <p class="copy caution">Caution: External use only. Do not get into your eyes</p>

    <svg class="care-icons" viewBox="0 0 172 56" aria-label="Period after opening 12 months, PET recyclable, vegan">
      <g fill="none" stroke="#333" stroke-width="2" stroke-linejoin="round">
        <path d="M4 26 h42 v22 a4 4 0 0 1 -4 4 h-34 a4 4 0 0 1 -4 -4z"/>
        <path d="M6 22 L44 12 L46 18 L8 26z"/>
        <path d="M82 8 l-10 18 h7 M88 8 l10 18 h-7 M70 36 l8 -12 M100 36 l-8 -12 M72 38 h26"/>
      </g>
      <text x="25" y="45" font-family="Josefin Sans, sans-serif" font-weight="600" font-size="11" text-anchor="middle" fill="#333">12M</text>
      <text x="85" y="34" font-family="Josefin Sans, sans-serif" font-weight="600" font-size="12" text-anchor="middle" fill="#333">1</text>
      <text x="85" y="52" font-family="Josefin Sans, sans-serif" font-weight="600" font-size="10" text-anchor="middle" fill="#333">PET</text>
      <path d="M130 52 C118 40 118 22 132 16 C138 26 138 42 130 52z" fill="#333"/>
      <path d="M134 50 C138 30 150 18 168 8 C166 30 154 46 134 50z" fill="#333"/>
    </svg>

    <div class="pill volume">100 mL / 3.38 fl.oz</div>

    <div class="floral-art" role="img" aria-label="Pink line-drawn wildflower stems climbing the centre of the label"></div>

    <div class="wordmark">Veyra</div>
    <div class="strength">96%</div>
    <h1 class="hero-name">SNAIL<br>MUCIN</h1>
    <p class="subtitle">POWER ESSENCE<br>WITH <span class="accent">GOTU KOLA</span></p>
    <p class="free-from">Paraben, Alcohol, Fragrance,<br>Phthalate and Cruelty Free</p>
    <p class="korean tagline-ko">뛰어난 수분 공급</p>

    <h2 class="heading ingredients-title">KEY<br>INGREDIENTS</h2>
    <p class="actives centered">Snail Mucin 96%<br>Secretion Filtrate &amp;<br>Gotu Kola.</p>
    <div class="rule rule-top"></div>
    <p class="copy description">Anti-aging Snail Mucin Essence penetrates deeply, provides critical, all day hydration, repairs damage, rebalances and prepares the skin for deeper absorption of serums and moisturizers.</p>
    <p class="korean benefits-ko">피부 보습, 다크 스팟 복구, 손상된 피부 재생</p>
    <div class="rule rule-bottom"></div>
    <p class="copy benefits">Benefits: Anti-aging, Collagen Boosting, Healing, Renewal, Scar Treatment, Elasticity, Tone</p>
    <div class="pill website">www.veyraskin.com</div>
    <p class="promise">Korean-inspired excellence</p>
  </main>
</body>
</html>
```